Stock Broking Firm - Web Design Project

We are looking at doing a full re-design of our home page and content page and moving the majority of our content over to DNN.

Phase 1 : Website redesign www.kpwealthdesk.com.au

The current design is too washed out, boring and has no call to action buttons.

Solution:

KP Wealthdesk is looking for a brighter/ cleaner redesign with a few stand out call to action buttons.

• Banner with logo across the top horizontally - Bright blue logo on white background similar to www.dailyledgerpress.com.au - CALL 1300 482 917 - Follow on Twitter / Facebook
• Horizontal menu bar - professional looking. - Home - About Us- Our Services - Membership - Open an Account - Become a member - Contact
• Below banner top left - large rotating banner - maybe zuvelo gallery style www.tallowhurst.com.au
• Right of rotating banner - Membership login
• Below members login - Register for Daily Market Report/ research blog - Large bright button / Name / Email / Phone / pop up??
• Below Register for daily market report - Market Indicies - RSS feed of delayed data from QNW see www.tallowhurst.com
• Below Market indicies - KP WEALTHDESK - Market Tweets ( feed from our twitter page)

Below Rotating Banner -

content area

Below content area - 4 large block buttons see www.greywickcapital.com.au ( hover over change colour)

Button 1 - EDUCATION - content - click here for more

Button 2 - Market Information and Research

Button 3 - Full service Broker - content brief - click here for more

Button 4 - Trade Commodities and Options

below buttons - small horizontal menu bar slightly different colour incl - Careers/ Partners / Legal Privacy FSG Site Map

Regards,
Colm Ashdown

Target Market(s)

35 - 65

Industry/Entity Type

Education

Requirements
Must have
• Follow brief above - large banner, call to action buttons, F.B. Twitter, Member login etc. 4 big buttons
Nice to have
• clean looking site similar to www.dailyledgerpress.com.au / not too busy. Corporate looking.
Should not have
• not too busy

```html
<!DOCTYPE html>
<html lang="en">
<head>
<meta charset="utf-8">
<title>KP Wealthdesk — Home</title>
<link rel="stylesheet" href="https://fonts.googleapis.com/css2?family=Open+Sans:wght@400;600;700&family=Arimo:wght@400;700&display=swap">
<style>
:root{
  --brand:#1a86ad;
  --brand-dark:#0d5a78;
  --ink:#222;
  --muted:#555;
  --band:#dcdcdc;
  --panel:#333;
  --panel-deep:#111;
  --field:#8c8c8c;
  --rule:#d4d4d4;
  --white:#fff;
}
*{box-sizing:border-box;margin:0;padding:0}
html,body{width:704px;height:1200px;overflow:hidden;background:var(--white)}
body{position:relative;font-family:"Open Sans",sans-serif;color:var(--ink)}
.abs{position:absolute}

/* header */
.top-links{left:372px;top:22px;width:251px;text-align:right;font-size:11px;color:#444;white-space:nowrap}
.call{left:420px;top:51px;width:207px;text-align:right;font-size:15px;color:#222;white-space:nowrap}
.call span{color:var(--brand)}
.social{top:73px;width:19px;height:19px;border-radius:50%;background:#c9c9c9}
.brand{left:72px;top:68px;display:flex;align-items:center;gap:8px;font-size:31px;color:var(--brand-dark);font-weight:400;letter-spacing:-.3px;white-space:nowrap}
.brand i{display:block;width:20px;height:20px;background:var(--brand-dark)}

/* nav */
.nav{left:0;top:117px;width:704px;height:22px;background:linear-gradient(#4a4a4a,#222)}
.nav a{position:absolute;top:0;height:22px;line-height:22px;font-size:10.5px;color:var(--white);text-decoration:none;padding:0 3px;white-space:nowrap}
.nav a.current{background:var(--brand)}

/* hero band */
.band{left:0;top:139px;width:704px;height:176px;background:var(--band)}
.hero{left:71px;top:147px;width:364px;height:168px;background:radial-gradient(circle at 40% 45%,#8fb2cc 0,#3b5d78 35%,#1d2e3e 75%)}
.hero-caption{left:71px;top:292px;width:364px;height:23px;background:rgba(14,110,150,.85);color:var(--white);font-size:9px;line-height:10px;padding:2px 5px}

.login-title{left:484px;top:168px;font-size:18px;font-weight:700;color:var(--brand);white-space:nowrap}
.lock{left:446px;top:156px}
.field-label{font-size:10.5px;color:#222;text-align:right;width:64px;left:438px;white-space:nowrap}
.input{left:505px;width:118px;height:24px;background:var(--white);border:1px solid #b8b8b8}
.login-note{left:470px;top:265px;width:151px;text-align:right;font-size:7px;color:#333;white-space:nowrap}
.btn-login{top:283px;width:83px;height:21px;border-radius:3px;background:linear-gradient(#1a8ab2,#0c5573);color:var(--white);font-size:9.5px;font-weight:700;text-align:center;line-height:21px}

/* content */
.content{left:72px;width:362px;font-size:9.2px;line-height:10.6px;color:#222}
.content h1{font-size:12px;font-weight:600;color:var(--brand)}
.content h2{font-size:11px;font-weight:600;color:#222}
.content b{color:var(--brand);font-weight:600}
.btn-small{background:var(--brand-dark);color:var(--white);font-size:9px;text-align:center;line-height:16px;height:16px}

/* report */
.report{left:447px;top:325px;width:177px;height:234px;background:var(--panel)}
.report-visual{left:447px;top:325px;width:177px;height:79px;background:linear-gradient(135deg,#0a1d4a,#1f5fbf 55%,#0b2b6e)}
.report-title{left:459px;top:410px;font-size:10.5px;color:var(--white)}
.report-text{left:456px;top:433px;width:152px;font-size:7px;line-height:8.2px;color:var(--white)}
.report-field{left:456px;width:153px;height:20px;background:var(--field);color:var(--white);font-size:8.5px;font-weight:700;line-height:20px;padding-left:7px}
.report-submit{left:456px;top:531px;width:64px;height:17px;background:var(--brand);color:var(--white);font-size:9px;text-align:center;line-height:17px}

/* market */
.market{left:447px;top:573px;width:177px;height:257px;border:1px solid #c4c4c4;background:var(--white);font-family:"Arimo",sans-serif}
.market-head{height:24px;background:linear-gradient(#1b8bb2,#0c5a79);color:var(--white);font-family:"Open Sans",sans-serif;font-size:10.5px;line-height:24px;padding-left:6px}
.market-row{height:21.2px;border-bottom:1px solid var(--rule);font-size:6.8px;line-height:21px;padding-left:4px;color:#111;white-space:nowrap;overflow:hidden}
.market-foot{display:flex;justify-content:space-between;align-items:center;padding:0 5px;height:20px;font-size:9px}
.market-foot .src{font-weight:700;color:var(--brand-dark);font-size:8px}

/* cards */
.card{top:851px;width:129px;height:118px;border-radius:8px;background:linear-gradient(#1c8db4,#0b5674);color:var(--white);padding:9px 9px 0}
.card h3{font-size:11.5px;font-weight:400;line-height:12px;height:24px}
.card p{font-size:7.3px;line-height:8.5px;color:#bfe3f0;margin-top:1px}
.card .btn-card{position:absolute;left:11px;top:93px;width:62px;height:16px;background:#2b2b2b;font-size:8.5px;line-height:16px;text-align:center}

/* footer */
.footer{left:0;top:978px;width:704px;height:194px;background:var(--panel);border-top:2px solid var(--brand)}
.contact-title{left:120px;top:1026px;font-size:10.5px;color:var(--white)}
.contact-rule{left:72px;top:1045px;width:129px;height:1px;background:#777}
.contact-text{left:72px;top:1053px;width:130px;font-size:7.4px;line-height:8.6px;color:var(--white)}
.testi-title{left:212px;top:996px;font-size:10.5px;color:var(--white)}
.testi{left:212px;width:270px;font-size:9px;line-height:10.4px;color:#9a9a9a}
.testi-name{left:212px;width:269px;text-align:right;font-size:8.5px;font-weight:700;font-style:italic;color:var(--white)}
.tweets-title{left:493px;top:997px;font-size:10.5px;font-weight:700;color:var(--white)}
.tweets-brand{left:493px;top:1027px;width:131px;height:22px;background:var(--white);font-size:16px;line-height:22px;color:var(--brand-dark);padding-left:4px;white-space:nowrap}
.tweet{left:513px;width:112px;font-size:7.3px;line-height:8.3px;color:#8a8a8a}
.tweet-dot{left:496px;width:9px;height:9px;border-radius:50%;background:var(--white)}
.subnav{left:0;top:1172px;width:704px;height:28px;background:var(--panel-deep);display:flex;justify-content:center;gap:22px;font-size:9px;line-height:28px;color:var(--white)}
</style>
</head>
<body>

<header>
  <div class="abs top-links">shares &nbsp;|&nbsp; options &nbsp;|&nbsp; commodities &nbsp;|&nbsp; FX</div>
  <div class="abs call"><span>CALL</span> 1300 482 917</div>
  <div class="abs social" style="left:577px" aria-hidden="true"></div>
  <div class="abs social" style="left:606px" aria-hidden="true"></div>
  <div class="abs brand"><i></i>KP Wealthdesk</div>
</header>

<nav class="abs nav">
  <a class="current" style="left:72px;width:39px">HOME</a>
  <a style="left:115px">ABOUT US</a>
  <a style="left:177px">OUR SERVICES</a>
  <a style="left:260px">MEMBERSHIP</a>
  <a style="left:336px">BECOME A MEMBER</a>
  <a style="left:450px">OPEN AN ACCOUNT</a>
  <a style="left:565px">CONTACT</a>
</nav>

<section>
  <div class="abs band"></div>
  <div class="abs hero" role="img" aria-label="Rotating banner: businessman touching a glowing dollar symbol on a digital screen"></div>
  <div class="abs hero-caption">KP Wealthdesk is a full-service brokerage company located on the Gold Coast (Australia).</div>

  <svg class="abs lock" width="30" height="38" viewBox="0 0 30 38" aria-hidden="true">
    <path d="M7 16V10a8 8 0 0 1 16 0v6" fill="none" stroke="#333" stroke-width="4"/>
    <rect x="1" y="15" width="28" height="22" rx="4" fill="#333"/>
    <rect x="13" y="22" width="4" height="8" rx="2" fill="#dcdcdc"/>
  </svg>
  <div class="abs login-title">MEMBERS LOGIN</div>
  <div class="abs field-label" style="top:215px">Username :</div>
  <div class="abs input" style="top:210px"></div>
  <div class="abs field-label" style="top:244px">Password :</div>
  <div class="abs input" style="top:239px"></div>
  <div class="abs login-note">register or forgot your password</div>
  <div class="abs btn-login" style="left:448px">LOGIN</div>
  <div class="abs btn-login" style="left:541px">REGISTER</div>
</section>

<main>
  <div class="abs content" style="top:322px"><h1>Welcome to KP Wealthdesk</h1></div>
  <p class="abs content" style="top:348px">KP Wealthdesk is a full-service brokerage company located on the Gold Coast (Australia). Our company trades Australian stocks, options on Australian stocks, commodities (gold, silver, light oil) and CFD through Corvane trading platform on behalf of our clients.</p>
  <div class="abs content" style="top:397px"><h2>Our main advantages are :</h2></div>
  <p class="abs content" style="top:422px"><b>Higher potential return</b>. Trading options on Australian stocks or commodities such as gold and silver, you spend much less money and make almost the same profit as if you buy or sell Australian stocks.</p>
  <p class="abs content" style="top:464px"><b>Low Brokerage commission and cost efficiency.</b> Options have great leveraging power. You can obtain an option position that will mimic your stock position almost identically, but at a huge cost savings.</p>
  <p class="abs content" style="top:506px"><b>Comprehensive education</b>. Many investors have avoided options and commodities, believing them to be sophisticated and, therefore, too difficult to understand. Many more have had bad initial experiences with options because neither they nor their brokers were properly trained in how to use them. The improper use of options, like that of any powerful tool, can lead to major problems. If you become a KP Wealthdesk Member, we will teach you how to trade options for FREE!!! Furthermore, you will get access to our research and daily reports.</p>
  <div class="abs content" style="top:589px"><h2>Our main objective is :</h2></div>
  <p class="abs content" style="top:613px">To increase clients’ wealth by regularly reviewing their trading portfolio, providing research and education and simplifying their trading through a personalised and professional service.</p>
  <p class="abs content" style="top:656px">We believe that constant communication with our clients’ allows for transparency in what we do and<br>ensures a long term relationship built on trust and commitment.</p>
  <p class="abs content" style="top:698px">Whether you are an experienced trader or have just started your portfolio, KP Wealthdesk welcomes you with<br>a commitment to profitable trading and superior client/advisor relationships.</p>
  <p class="abs content" style="top:740px">Our unique blend of experience across funds management and technical analysis coupled with enthusiasm<br>and drive for success, creates the perfect climate for you to capitalise on your resources.</p>
  <div class="abs btn-small" style="left:72px;top:797px;width:63px">Learn More</div>
</main>

<aside>
  <div class="abs report"></div>
  <div class="abs report-visual" role="img" aria-label="Blue stock market ticker board"></div>
  <div class="abs report-title">Daily Market Report</div>
  <p class="abs report-text">Sign up here to receive regular<br>e-newsletter. Please note you will only be added to the list if a full name is submitted.</p>
  <div class="abs report-field" style="top:477px">Email</div>
  <div class="abs report-field" style="top:503px">Name</div>
  <div class="abs report-submit">Submit</div>

  <div class="abs market">
    <div class="market-head">Market indicies</div>
    <div class="market-row">01:53 AM Vasser tells Greece to stay the course</div>
    <div class="market-row">11:25 PM Vasser confronts Greek austerity anger</div>
    <div class="market-row">07:49 PM Lockdown in Athens ahead of Vasser's visit</div>
    <div class="market-row">05:59 PM Ortaine plans to cut costs after saving $0.5b</div>
    <div class="market-row">04:58 PM Kestrel Ore sells NZ steel for $74m</div>
    <div class="market-row">04:51 PM $A higher on euro moves, CBQ comments</div>
    <div class="market-row">04:26 PM GFO cuts Asian growth forecast</div>
    <div class="market-row">04:23 PM Aust stocks hit 14-month high</div>
    <div class="market-row">04:21 PM $A higher on European market moves</div>
    <div class="market-row">04:00 PM Aust stocks hit 14-month high</div>
    <div class="market-foot"><span class="src">QNW</span><span>Read More...</span></div>
  </div>
</aside>

<section>
  <div class="abs card" style="left:72px"><h3>Education</h3><p>Lorem Ipsum is simply dummy text of the printing and typesetting industry. Lorem Ipsum has been the industry's standard dummy text has been typesetting industry.</p><div class="btn-card">Learn More</div></div>
  <div class="abs card" style="left:212px"><h3>Market Information<br>&amp; Research</h3><p>Lorem Ipsum is simply dummy text of the printing and typesetting industry. Lorem Ipsum has been the industry's standard dummy text.</p><div class="btn-card">Learn More</div></div>
  <div class="abs card" style="left:353px"><h3>Full service Broker</h3><p>Lorem Ipsum is simply dummy text of the printing and typesetting industry. Lorem Ipsum has been the industry's standard dummy text has been typesetting industry.</p><div class="btn-card">Learn More</div></div>
  <div class="abs card" style="left:493px"><h3>Trade Commodities<br>and Options</h3><p>Lorem Ipsum is simply dummy text of the printing and typesetting industry. Lorem Ipsum has been the industry's standard dummy text.</p><div class="btn-card">Learn More</div></div>
</section>

<footer>
  <div class="abs footer"></div>
  <svg class="abs" style="left:72px;top:1012px" width="44" height="32" viewBox="0 0 44 32" aria-hidden="true">
    <rect x="1" y="6" width="42" height="25" fill="#e9e9e9"/>
    <path d="M1 6 L22 22 L43 6" fill="none" stroke="#999" stroke-width="1.5"/>
  </svg>
  <div class="abs contact-title">Contact details</div>
  <div class="abs contact-rule"></div>
  <p class="abs contact-text">For more information on how you can benefit from being a KP Wealthdesk Member, call one of our friendly consultants today on +61 (0) 7 5519 2860, sign up for a free 7 DAY TRIAL or contact us via our contact page for a FREE one on one consultation.</p>

  <div class="abs testi-title">Testimonials</div>
  <p class="abs testi" style="top:1021px">Lorem Ipsum is simply dummy text of the printing and typesetting industry. Lorem Ipsum has been the industry's standard dummy text ever since the 1500s, when an unknown printer took a galley of type and scrambled</p>
  <div class="abs testi-name" style="top:1070px">Petra L.</div>
  <p class="abs testi" style="top:1093px">Lorem Ipsum is simply dummy text of the printing and typesetting industry. Lorem Ipsum has been the industry's standard dummy text ever since the 1500s, when an unknown printer took a galley of type and scrambled</p>
  <div class="abs testi-name" style="top:1140px">Declan R.</div>

  <div class="abs tweets-title">Latest tweets</div>
  <div class="abs tweets-brand">KP Wealthdesk</div>
  <div class="abs tweet-dot" style="top:1069px"></div>
  <p class="abs tweet" style="top:1067px">Lorem Ipsum is simply dummy text of the printing and typesetting industry.</p>
  <div class="abs tweet-dot" style="top:1106px"></div>
  <p class="abs tweet" style="top:1104px">Lorem Ipsum is simply dummy text of the printing and typesetting industry.</p>

  <nav class="abs subnav"><span>Careers</span><span>Partners</span><span>Legal Privacy</span><span>FSG</span><span>Site Map</span></nav>
</footer>

</body>
</html>
```